Brightvale Fluid Systems Corp Business Cards

Business cards to match the logo.

Company is a start up water technology company that has developed a patented system using centrifugal force to separate waste from municipal waste water to produce crystal clear clean water. Product sell starting at 2 million to governments both in the US and international.

Business cards should have a professional look with the target generally engineers.

Target Market(s)

Engineers, Government officials and investors

Industry/Entity Type

Water Treatment

Contact Information for Business Card

Business cards design will be used for 6 to 8 people with job titles. Can use the quote "If there is magic in the planet, it is contained in water." but not required to use quote. Should follow theme of Logo

Font styles to use
Other font styles liked:
• match logo font

Requirements
Nice to have
• Colors to match Logo. Business cards to match style of flow of Logo.
• Emphasis on clean look not a busy look. Clean flowing water.
Should not have
• Pictures of industrial equipment or wastewater

```html
<!DOCTYPE html>
<html lang="en">
<head>
<meta charset="utf-8">
<title>Brightvale Fluid Systems Corp – Business Cards</title>
<link rel="stylesheet" href="https://fonts.googleapis.com/css2?family=Crimson+Text:wght@400;700&display=swap">
<style>
  :root {
    --page-bg: #e9ecef;
    --navy-top: #0d3f86;
    --navy-bottom: #05234f;
    --aqua-top: #86e0f2;
    --aqua-bottom: #2784bd;
    --wave-deep: #0f5aa6;
    --wave-mid: #1e74c0;
    --wave-light: #4aa6dc;
    --ink-light: #ffffff;
    --ink-soft: #d6e6f7;
    --logo-front: #1a64a3;
    --logo-back: #e8f3ff;
    --line: rgba(255,255,255,0.85);
  }
  * { box-sizing: border-box; margin: 0; padding: 0; }
  html, body { width: 1200px; height: 800px; overflow: hidden; }
  body {
    background: var(--page-bg);
    font-family: "Crimson Text", Georgia, serif;
    position: relative;
  }
  .card {
    position: absolute;
    width: 560px;
    height: 320px;
    overflow: hidden;
    box-shadow: 0 8px 22px rgba(0,0,0,0.18);
  }
  .card-back {
    left: 360px; top: 50px;
    background: linear-gradient(160deg, var(--navy-top) 0%, var(--navy-bottom) 100%);
    color: var(--ink-light);
  }
  .card-front {
    left: 240px; top: 420px;
    background: linear-gradient(180deg, var(--aqua-top) 0%, var(--aqua-bottom) 100%);
  }
  .card svg.decor { position: absolute; inset: 0; width: 100%; height: 100%; }

  .holder { position: absolute; left: 44px; top: 46px; }
  .holder-name { font-size: 24px; font-weight: 700; line-height: 1; }
  .holder-title { font-size: 10px; color: var(--ink-soft); letter-spacing: 0.5px; margin-top: 2px; }

  .contact-list { position: absolute; left: 44px; top: 106px; list-style: none; font-size: 11.5px; line-height: 16px; }
  .contact-list li { display: flex; align-items: center; gap: 9px; }
  .contact-list svg { width: 10px; height: 10px; fill: var(--wave-light); flex: none; }

  .address { position: absolute; left: 44px; top: 180px; font-size: 11.5px; line-height: 14px; }

  .brand-back {
    position: absolute; right: 40px; top: 60px;
    font-size: 20px; font-weight: 400; color: var(--logo-back);
    letter-spacing: 1.5px; text-align: right; line-height: 1.05;
  }
  .brand-front {
    position: absolute; left: 52px; top: 58px;
    font-size: 46px; font-weight: 400; color: var(--logo-front);
    letter-spacing: 2px; line-height: 1;
  }
  .quote {
    position: absolute; right: 22px; bottom: 26px;
    font-size: 10.5px; color: var(--ink-light);
  }
</style>
</head>
<body>

  <section class="card card-back" aria-label="Business card, contact side">
    <svg class="decor" viewBox="0 0 560 320" aria-hidden="true">
      <g class="accent-lines" stroke="var(--line)" stroke-width="1" fill="none">
        <line x1="350" y1="220" x2="545" y2="140"/>
        <line x1="356" y1="226" x2="548" y2="148"/>
        <line x1="366" y1="229" x2="550" y2="154"/>
      </g>
      <path d="M0 250 C120 235 220 250 320 285 C380 305 460 312 560 300 L560 320 L0 320 Z" fill="var(--wave-deep)" opacity="0.55"/>
      <path d="M0 262 C110 250 210 268 300 296 C360 312 450 318 560 310 L560 320 L0 320 Z" fill="var(--wave-mid)" opacity="0.7"/>
      <path d="M20 244 C110 238 190 248 260 268" stroke="var(--wave-light)" stroke-width="2" fill="none"/>
    </svg>

    <div class="holder">
      <p class="holder-name">Daniel Marsh</p>
      <p class="holder-title">CEO</p>
    </div>

    <ul class="contact-list">
      <li><svg viewBox="0 0 10 10"><path d="M2 0.5 L3.6 0.5 L4.2 3 L3 3.8 C3.6 5.2 4.8 6.4 6.2 7 L7 5.8 L9.5 6.4 L9.5 8 C9.5 9 8.8 9.5 8 9.5 C4 9.2 0.8 6 0.5 2 C0.5 1.2 1 0.5 2 0.5 Z"/></svg>555-014-2291</li>
      <li><svg viewBox="0 0 10 10"><path d="M3 0.5 H7 A1 1 0 0 1 8 1.5 V8.5 A1 1 0 0 1 7 9.5 H3 A1 1 0 0 1 2 8.5 V1.5 A1 1 0 0 1 3 0.5 Z M3 1.8 V7.6 H7 V1.8 Z"/></svg>555-018-4231</li>
      <li><svg viewBox="0 0 10 10"><path d="M0.5 2 H9.5 V8.5 H0.5 Z M1.2 2.6 L5 5.6 L8.8 2.6 Z" fill-rule="evenodd"/></svg>dmarsh@brightvalefs.com</li>
      <li><svg viewBox="0 0 10 10"><path d="M5 0.5 A4.5 4.5 0 1 0 5 9.5 A4.5 4.5 0 1 0 5 0.5 Z M5 1.5 A3.5 3.5 0 1 1 5 8.5 A3.5 3.5 0 1 1 5 1.5 Z M1 4.6 H9 V5.4 H1 Z M4.6 1 H5.4 V9 H4.6 Z"/></svg>www.brightvalefs.com</li>
    </ul>

    <p class="address">240 Harbor Ave., Suite 310<br>Portside, FL 33900</p>

    <p class="brand-back">BRIGHTVALE<br>FLUID SYSTEMS</p>

    <p class="quote">“If there is magic in the planet, it is contained in water.”</p>
  </section>

  <section class="card card-front" aria-label="Business card, brand side">
    <svg class="decor" viewBox="0 0 560 320" aria-hidden="true">
      <g class="accent-lines" stroke="var(--line)" stroke-width="1" fill="none">
        <line x1="330" y1="190" x2="545" y2="100"/>
        <line x1="338" y1="197" x2="548" y2="108"/>
        <line x1="348" y1="200" x2="550" y2="115"/>
      </g>
      <path d="M0 215 C90 195 170 200 250 225 C330 250 420 280 560 290 L560 320 L0 320 Z" fill="var(--wave-deep)" opacity="0.55"/>
      <path d="M0 240 C100 225 190 235 270 258 C350 282 440 300 560 305 L560 320 L0 320 Z" fill="var(--wave-mid)" opacity="0.6"/>
      <path d="M20 200 C100 186 170 190 230 206" stroke="var(--wave-light)" stroke-width="3" fill="none" opacity="0.8"/>
      <path d="M120 250 C220 240 330 262 440 282" stroke="var(--wave-light)" stroke-width="6" fill="none" opacity="0.5"/>
    </svg>

    <p class="brand-front">BRIGHTVALE<br>FLUID SYSTEMS</p>
  </section>

</body>
</html>
```